QMA Letter Head (Official & Elegant)

We need a letterhead design for our new set up school named Harwick Speech Academy.

We are providing professional English language courses to our students.
1. Instead of teaching them grammar, we persist on native, we teach students to speak and learn natively.
2. We persist on intercultural, we want students to immerse in the culture of native English speakers. Learn about the culture of native speakers from A-Z.

The colour code should follow the logo colour code.

Here are the information, they should be contained in the letter head.
1. Our School Logo [We love our elegant logo very much, it should be a core to lead the design]
2. Our Company Name : Harwick Speech Academy Sdn. Bhd. (2284517-K)
3. Our company address [Our branches will be increased in the future, so you should make this part flexible to be added on in the future]

Headquarter : Lot 47815-B, 47815-C, Jalan 7/19C, Taman Seri Ros, Batu 8, Jalan Merbau, 51200 Kuala Lumpur, Malaysia.
Tel : 03-7481 9302 / 03-7481 6718 (Hunting Line)

Teaching Centre (Permai Indah) : No. 27C, Jalan PI 6, Taman Permai Indah, 68100 Batu Caves, Selangor Darul Ehsan, Malaysia.
Tel : 03-5893 4170

4. facebook: https://www.facebook.com/harwickspeechacademy

5. Email : enquiry@harwick-example.edu.my

6. We prefer to see the flags of different native English speaking countries, USA, England, Australia, New Zealand, and some other significant or meaningful related English cultures.

Our directors are a serious entrepreneurs, the final design should be elegant and able to convey the message that we are professional with international impression.

Industry/Entity Type

School

Requirements
Must have
• 1. Making a bit vertical rectangular bar, get all information designed on the left.
• 2. Watermark.
Nice to have
• 1. Flags of the English Speaking Country.
• 2. Making the rectangular bar like a gold medal with 5 stars at the bottom.

```html
<!DOCTYPE html>
<html lang="en">
<head>
<meta charset="utf-8">
<title>Harwick Speech Academy – Letterhead</title>
<link href="https://fonts.googleapis.com/css2?family=Lato:ital,wght@0,300;0,400;0,700;1,300;1,400&family=Carlito&display=swap" rel="stylesheet">
<style>
  :root {
    --backdrop: #cfcfcf;
    --paper: #ffffff;
    --ink: #1a1a1a;
    --body-ink: #2b2b2b;
    --band: #0c0c0c;
    --gold: #c9a45a;
    --gold-soft: #e8dcc3;
    --signature-tone: #eeeeee;
  }
  * { box-sizing: border-box; margin: 0; padding: 0; }
  html, body { width: 1200px; height: 1000px; overflow: hidden; }
  body { background: var(--backdrop); position: relative; font-family: "Lato", Arial, sans-serif; color: var(--ink); }

  .letterhead { position: absolute; left: 287px; top: 4px; width: 701px; height: 992px; background: var(--paper); box-shadow: 0 0 12px rgba(0,0,0,.25); }

  /* Side bar */
  .sidebar { position: absolute; left: 0; top: 0; width: 215px; height: 100%; }
  .sidebar-rule { position: absolute; left: 215px; top: 0; width: 3px; height: 100%; background: var(--gold); }

  .brand-band { position: absolute; left: 0; top: 0; width: 215px; height: 201px; background: var(--band); display: flex; flex-direction: column; align-items: center; justify-content: center; gap: 12px; }
  .brand-mark { width: 14px; height: 14px; border-radius: 50%; background: var(--gold); }
  .brand-name { color: var(--gold); font-weight: 400; font-size: 21px; line-height: 26px; text-align: center; letter-spacing: .5px; }

  .company { position: absolute; left: 12px; top: 209px; width: 200px; font-weight: 400; font-style: italic; font-size: 16.5px; line-height: 23px; }
  .divider { position: absolute; left: 10px; width: 181px; height: 1px; background: var(--gold-soft); }

  .branch { position: absolute; left: 10px; width: 205px; font-size: 11.5px; line-height: 19px; }
  .branch-title { font-weight: 700; }
  .branch-address { padding-left: 3px; }
  .branch-tel { font-weight: 700; }
  .branch-tel .extra { display: block; padding-left: 25px; }

  .contact-email { position: absolute; left: 0; top: 848px; width: 215px; text-align: center; font-size: 12.5px; white-space: nowrap; }
  .contact-social { position: absolute; left: 0; top: 872px; width: 215px; text-align: center; font-size: 9px; white-space: nowrap; }

  .footer-band { position: absolute; left: 0; top: 891px; width: 215px; height: 101px; background: var(--band); }
  .flags { position: absolute; left: 25px; top: 18px; display: flex; gap: 8px; }
  .flags svg { width: 36px; height: 36px; display: block; }
  .website { position: absolute; left: 0; top: 68px; width: 215px; text-align: center; color: var(--gold); font-size: 12.5px; letter-spacing: .6px; white-space: nowrap; }

  /* Letter body */
  .letter { position: absolute; left: 242px; top: 0; width: 424px; font-family: "Carlito", "Calibri", sans-serif; color: var(--body-ink); font-size: 13.6px; line-height: 17px; }
  .salutation { position: absolute; top: 187px; }
  .letter-body { position: absolute; top: 263px; width: 424px; }
  .letter-body p { text-align: justify; text-indent: 36px; margin-bottom: 9px; letter-spacing: .5px; }
  .closing { position: absolute; top: 680px; }
  .signature { position: absolute; left: 26px; top: 708px; width: 122px; height: 66px; }
  .signer { position: absolute; top: 786px; line-height: 22px; }
</style>
</head>
<body>
  <main class="letterhead">
    <aside class="sidebar">
      <div class="brand-band">
        <span class="brand-mark"></span>
        <div class="brand-name">Harwick<br>Speech Academy</div>
      </div>

      <div class="company">Harwick Speech Academy Sdn. Bhd. (2284517-K)</div>
      <div class="divider" style="top:263px"></div>

      <section class="branch" style="top:272px">
        <div class="branch-title">Headquarter :</div>
        <div class="branch-address">Lot 47815-B, 47815-C, Jalan 7/19C, Taman Seri Ros, Batu 8, Jalan Merbau, 51200 Kuala Lumpur, Malaysia.</div>
        <div class="branch-tel">Tel : 03-7481 9302<span class="extra">03-7481 6718 (Hunting Line)</span></div>
      </section>
      <div class="divider" style="top:394px"></div>

      <section class="branch" style="top:404px">
        <div class="branch-title">Teaching Centre (Permai Indah) :</div>
        <div class="branch-address">No. 27C, Jalan PI 6, Taman Permai Indah, 68100 Batu Caves, Selangor Darul Ehsan, Malaysia.</div>
        <div class="branch-tel">Tel : 03-5893 4170</div>
      </section>
      <div class="divider" style="top:524px"></div>

      <div class="divider" style="top:832px"></div>
      <div class="contact-email">enquiry@harwick-example.edu.my</div>
      <div class="contact-social">www.facebook.com/harwickspeechacademy</div>

      <div class="footer-band">
        <div class="flags">
          <svg viewBox="0 0 36 36" role="img" aria-label="Flag of the United States">
            <defs><linearGradient id="flag-us" x1="0" y1="0" x2="1" y2="1"><stop offset="0" stop-color="#2f4a8f"/><stop offset=".5" stop-color="#e8e8e8"/><stop offset="1" stop-color="#c22d36"/></linearGradient></defs>
            <circle cx="18" cy="18" r="17" fill="url(#flag-us)"/>
          </svg>
          <svg viewBox="0 0 36 36" role="img" aria-label="Flag of the United Kingdom">
            <defs><linearGradient id="flag-uk" x1="0" y1="0" x2="1" y2="1"><stop offset="0" stop-color="#253f85"/><stop offset=".5" stop-color="#d9d9d9"/><stop offset="1" stop-color="#c8232c"/></linearGradient></defs>
            <circle cx="18" cy="18" r="17" fill="url(#flag-uk)"/>
          </svg>
          <svg viewBox="0 0 36 36" role="img" aria-label="Flag of Australia">
            <defs><linearGradient id="flag-au" x1="0" y1="0" x2="1" y2="1"><stop offset="0" stop-color="#1f3a86"/><stop offset="1" stop-color="#3b57a3"/></linearGradient></defs>
            <circle cx="18" cy="18" r="17" fill="url(#flag-au)"/>
          </svg>
          <svg viewBox="0 0 36 36" role="img" aria-label="Flag of Canada">
            <defs><linearGradient id="flag-ca" x1="0" y1="0" x2="1" y2="0"><stop offset="0" stop-color="#d52b1e"/><stop offset=".5" stop-color="#f2f2f2"/><stop offset="1" stop-color="#d52b1e"/></linearGradient></defs>
            <circle cx="18" cy="18" r="17" fill="url(#flag-ca)"/>
          </svg>
        </div>
        <div class="website">www.harwick-example.edu.my</div>
      </div>
    </aside>
    <div class="sidebar-rule"></div>

    <article class="letter">
      <div class="salutation">Dear,</div>
      <div class="letter-body">
        <p>Lorem ipsum dolor sit amet, consectetur adipiscing elit, sed do eiusmod tempor incididunt ut labore et dolore magna aliqua. Ut enim ad minim veniam, quis nostrud exercitation ullamco laboris nisi ut aliquip ex ea commodo consequat. Duis aute irure dolor in reprehenderit in voluptate velit esse cillum dolore eu fugiat nulla pariatur. Excepteur sint occaecat cupidatat non proident, sunt in culpa qui officia deserunt mollit anim id est laborum.</p>
        <p>Lorem ipsum dolor sit amet, consectetur adipiscing elit, sed do eiusmod tempor incididunt ut labore et dolore magna aliqua. Ut enim ad minim veniam, quis nostrud exercitation ullamco laboris nisi ut aliquip ex ea commodo consequat. Duis aute irure dolor in reprehenderit in voluptate velit esse cillum dolore eu fugiat nulla pariatur. Excepteur sint occaecat cupidatat non proident, sunt in culpa qui officia deserunt mollit anim id est laborum.</p>
        <p>Lorem ipsum dolor sit amet, consectetur adipiscing elit, sed do eiusmod tempor incididunt ut labore et dolore magna aliqua. Ut enim ad minim veniam, quis nostrud exercitation ullamco laboris</p>
        <p>Lorem ipsum dolor sit amet, consectetur adipiscing elit, sed do eiusmod tempor incididunt ut labore et dolore magna aliqua.</p>
      </div>
      <div class="closing">Kind Regards,</div>
      <svg class="signature" viewBox="0 0 122 66" role="img" aria-label="Handwritten signature of the chairman">
        <rect width="122" height="66" rx="4" fill="var(--signature-tone)"/>
      </svg>
      <div class="signer">Adam Reyes,<br>Chairman of the board</div>
    </article>
  </main>
</body>
</html>
```